Collagen Tub Packaging Design for a New Brand

PLEASE DON'T SEND ANY NEW DESIGNS WE JUST HAVE TO DECIDE WITH MY PARTNERS THANKS A LOT.
I've created a very detailed document & design examples of what we like in certain designs and what we don't.

There are 3 documents:
1- Brief for the Design (please read it before designing)
2- Brand Design Examples that we like (and why we like them)
3- Die cut for the packaging design. This will be it's dimensions.

We are NOT looking for someone to micro-manage. In contrast, we want someone to help us express our ideas better with their design. Nothing I say in these briefs are there to limit the creativity of the designer, because if we knew exactly what we wanted we would do it ourselves but we trust the designer's expertise in this packaging design.

In short: We want our brand to feel premium, high-quality & trust worthy with it's design not feeling very busy or bloated. We don't have a logo source file, but you'll get the idea of what we want when you see it).

Let me know if you have any further questions, will answer each question real fast.

Thanks.

Target Market(s)

Pretty much everyone above 25+ in Turkey because nearly all of them are using are collagens so our audience is wild.

Industry/Entity Type

Collagen - Health, Wellness & Supplements

Font styles to use
Serif
Sans Serif

Colors

Designer to choose colors to be used in the design.

Requirements
Must have
• Our design should be distinct, a design style which everyone can identify from 10 meters away if they know the product. This is a MUST have for us. It's up to designer to achieve it. This can be just a simple color palette aswell.
Should not have
• It shouldn't feel bloated and very busy. Please avoid very detailed icons (as a rule of thumb, if you can make it work great)

```html
<!DOCTYPE html>
<html lang="en">
<head>
<meta charset="UTF-8">
<title>Lunaveda Collagen Peptides – Label</title>
<link rel="stylesheet" href="https://fonts.googleapis.com/css2?family=Noto+Serif:wght@500;600&family=Roboto+Condensed:wght@400&family=Lato:wght@400&display=swap">
<style>
  :root {
    --bg: #f1f1f1;
    --navy: #123257;
    --navy-deep: #1b2537;
    --silver: #c4c6c6;
    --silver-light: #d6d8d8;
    --silver-band: #e4e6e6;
    --white: #ffffff;
    --ink: #2a2a2a;
    --ghost: #c9cfd2;
  }
  * { margin: 0; padding: 0; box-sizing: border-box; }
  html, body {
    width: 1200px; height: 819px; overflow: hidden;
    background: var(--bg);
  }
  .canvas {
    position: relative; width: 1200px; height: 819px;
    background: var(--bg);
  }
  .label {
    position: absolute; left: 466px; top: 150px;
    width: 278px; height: 410px;
    background: var(--navy-deep);
    border-radius: 4px;
    overflow: hidden;
  }
  .label-trim {
    position: absolute; left: 0; top: 56px; width: 100%; height: 10px;
    background: var(--silver-band);
  }
  .label-front {
    position: absolute; left: 0; top: 72px; width: 100%; height: 180px;
    background: var(--navy);
    padding: 22px 20px 0 20px;
    color: var(--white);
  }
  .brand-name {
    font-family: "Noto Serif", serif; font-weight: 500;
    font-size: 23px; line-height: 1;
  }
  .product-variant {
    font-family: "Roboto Condensed", sans-serif;
    font-size: 12px; text-align: right; margin-top: 4px;
    color: #dfe4ea;
  }
  .product-name {
    font-family: "Noto Serif", serif; font-weight: 600;
    font-size: 44px; line-height: 1.2; letter-spacing: -1px;
    margin-top: -2px;
  }
  .label-facts {
    position: absolute; left: 0; top: 252px; width: 100%; height: 150px;
    background: linear-gradient(90deg, var(--silver-light), var(--silver) 60%, #b9bbbb);
    padding: 20px 16px 0 16px;
    color: var(--white);
  }
  .tagline {
    font-family: "Roboto Condensed", sans-serif;
    font-size: 15.5px; text-align: center;
  }
  .facts-rule {
    height: 1px; background: var(--white); opacity: .8;
    margin: 10px 4px 12px 4px;
  }
  .facts-list {
    display: flex; justify-content: space-between; padding: 0 4px;
    list-style: none;
  }
  .fact {
    width: 60px; height: 60px; border-radius: 50%;
    background: radial-gradient(circle at 40% 35%, #eceeee, #c3c5c5 75%);
    display: flex; flex-direction: column; align-items: center; justify-content: center;
    font-family: "Roboto Condensed", sans-serif; line-height: 1.1;
  }
  .fact-value { font-size: 13px; }
  .fact-unit { font-size: 9px; }
  .fact-label { font-size: 11px; }
  .brand-ghost {
    position: absolute; left: 0; top: 618px; width: 100%;
    text-align: center;
    font-family: "Noto Serif", serif; font-weight: 500;
    font-size: 86px; line-height: 1;
    color: var(--ghost);
  }
  .brand-copy {
    position: absolute; left: 295px; top: 720px; width: 610px;
    text-align: center;
    font-family: "Lato", sans-serif; font-size: 13.5px; line-height: 1.3;
    color: var(--ink);
  }
</style>
</head>
<body>
<main class="canvas">
  <section class="label" aria-label="Collagen peptides label">
    <div class="label-trim"></div>
    <div class="label-front">
      <p class="brand-name">Lunaveda</p>
      <p class="product-variant">Hydrolyzed</p>
      <h1 class="product-name">COLLAGEN<br>PEPTIDES</h1>
    </div>
    <div class="label-facts">
      <p class="tagline">High Absorption - High-Quality material</p>
      <div class="facts-rule"></div>
      <ul class="facts-list">
        <li class="fact"><span class="fact-value">11<span class="fact-unit">G</span></span><span class="fact-label">Protein</span></li>
        <li class="fact"><span class="fact-value">12<span class="fact-unit">G</span></span><span class="fact-label">Collagen</span></li>
        <li class="fact"><span class="fact-value">0<span class="fact-unit">G</span></span><span class="fact-label">Sugar</span></li>
      </ul>
    </div>
  </section>
  <p class="brand-ghost">Lunaveda</p>
  <p class="brand-copy">Lorem ipsum dolor sit amet, consectetur adipiscing elit, sed do eiusmod tempor incididunt ut labore et dolore magna aliqua. Quis ipsum suspendisse ultrices gravida. Risus commodo viverra maecenas accumsan lacus vel facilisis.</p>
</main>
</body>
</html>
```